Logo and Flyer for Co-Branded Comedy Show

Graphic designer needed to create a promotional flyer for a comedy show. Two different comedy shows, with distinct branding, are joining forces to create a combined show. (co-branded logo to be included is attached.)

The design of the promotional materials should be a modern take on a vintage poster a la Quirkwood Jamboree. We'd like it to be a vintage look with a modern twist (I have attached the Quirkwood Jamboree Flyer for reference - marked up with info for our show) Filename: PLGRVN Flyer Mark Up

Images of the two hosts are attached: Filenames:

Our show will be in a theater, so if it can play off a playbill that would be great. I have attached examples of the clean look that we like, as well as some vintage theater flyers. We'd like to stay on the lighter side of the color palette (light gray, blues, etc. which is in line with the Harbor Laughs Live flyer) Filename: PLGR VN Flyer Direction

Current Branding of the individual Shows
I have attached the current promo materials for the individual shows, so you have a sense of the color palette and logo treatment.

The deliverable:
1 flyer vertical, 1 flyer horizontal - same design/concept but in 2 orientation (vertical and horizontal) horizontal will be used for web.
***This flyer will include the co-branded logo seen attached - Harbor Laughs Live Gets Real Honest (individual logos already created and attached) - Download PSD File here: http://lnk.example-short.test/PLGRVN

Industry/Entity Type

Graphic Designer

Colors
0493cd
85cae6
ecf7fb
f5f5f5
ffffff
606060
fbfbfb
0255a3
3176b5

Requirements
Must have
• Vintage look with a modern twist
• Vertical and horizontal options

```html
<!DOCTYPE html>
<html lang="en">
<head>
<meta charset="utf-8">
<title>Harbor Laughs Live Gets Real Honest</title>
<link href="https://fonts.googleapis.com/css2?family=Poiret+One&family=Josefin+Sans:ital,wght@0,300;0,400;0,600;0,700;1,400&display=swap" rel="stylesheet">
<style>
  :root {
    --blue: #0493cd;
    --blue-deep: #0255a3;
    --blue-mid: #3176b5;
    --blue-light: #85cae6;
    --paper: #e6e2d6;
    --paper-light: #f5f3ee;
    --grey: #606060;
    --white: #ffffff;
    --photo-grey: #b9b9b9;
    --frame: #f1ede2;
    --clip: #f2b320;
  }
  * { margin: 0; padding: 0; box-sizing: border-box; }
  html, body { width: 778px; height: 1200px; overflow: hidden; }
  body { background: var(--white); }
  .flyer {
    position: relative;
    width: 778px; height: 1200px; overflow: hidden;
    background: radial-gradient(ellipse at 50% 45%, var(--paper-light) 0%, var(--paper) 80%);
    font-family: "Josefin Sans", sans-serif;
    color: var(--grey);
  }
  .top-strip { position: absolute; left: 0; top: 0; width: 100%; height: 8px; background: var(--blue); }
  .presenter-bar {
    position: absolute; left: 0; top: 8px; width: 100%; height: 64px;
    background: var(--white);
    display: flex; align-items: center; padding-left: 60px; gap: 18px;
    border-bottom: 7px solid var(--blue);
  }
  .presenter { font-weight: 700; font-size: 30px; color: var(--grey); letter-spacing: -0.5px; }
  .presents { font-style: italic; font-size: 30px; color: var(--blue); letter-spacing: 14px; }
  .title { position: absolute; left: 0; width: 100%; text-align: center; font-family: "Poiret One", sans-serif; color: var(--blue); white-space: nowrap; }
  .title-top { top: 104px; font-size: 40px; letter-spacing: 3px; }
  .title-main { top: 150px; font-size: 106px; letter-spacing: 1px; line-height: 1; font-weight: 400; }
  .hosted-by { position: absolute; top: 262px; right: 36px; text-align: right; font-size: 40px; font-weight: 300; color: var(--grey); white-space: nowrap; }
  .host-card {
    position: absolute; background: var(--frame); padding: 22px;
    box-shadow: 2px 4px 10px rgba(0,0,0,0.2);
  }
  .host-card.left { left: 72px; top: 372px; width: 388px; height: 368px; transform: rotate(-2deg); }
  .host-card.right { left: 392px; top: 384px; width: 362px; height: 364px; transform: rotate(1.5deg); }
  .host-photo {
    width: 100%; height: 100%;
    background: linear-gradient(135deg, #dedede 0%, var(--photo-grey) 55%, #8f8f8f 100%);
    position: relative;
  }
  .host-name { position: absolute; font-size: 12px; color: var(--grey); white-space: nowrap; }
  .host-card.left .host-name { right: 24px; bottom: 20px; }
  .host-card.right .host-name { left: 14px; bottom: 12px; }
  .clip { position: absolute; top: -16px; width: 50px; height: 26px; background: var(--clip); border-radius: 3px; }
  .host-card.left .clip { left: 30px; }
  .host-card.right .clip { left: 130px; }
  .rule { position: absolute; left: 0; width: 100%; height: 18px; }
  .rule::before, .rule::after { content: ""; position: absolute; left: 0; width: 100%; }
  .rule::before { top: 0; height: 8px; background: var(--blue-mid); }
  .rule::after { top: 12px; height: 5px; background: var(--blue-light); }
  .rule-upper { top: 806px; }
  .rule-lower { top: 1018px; }
  .rule-bottom { top: 1176px; }
  .date-line { position: absolute; top: 846px; left: 0; width: 100%; text-align: center; font-size: 42px; color: var(--blue); font-weight: 300; white-space: nowrap; }
  .lineup { position: absolute; left: 0; width: 100%; text-align: center; font-size: 30px; color: var(--blue-deep); font-weight: 300; white-space: nowrap; }
  .lineup-1 { top: 912px; }
  .lineup-2 { top: 962px; }
  .venue { position: absolute; top: 1054px; left: 0; width: 100%; text-align: center; font-size: 27px; color: var(--grey); font-weight: 300; white-space: nowrap; }
  .site { position: absolute; top: 1092px; left: 0; width: 100%; text-align: center; font-family: "Poiret One", sans-serif; font-size: 64px; line-height: 1.1; color: var(--blue); letter-spacing: 17px; font-weight: 400; white-space: nowrap; }
</style>
</head>
<body>
<main class="flyer">
  <div class="top-strip"></div>
  <header class="presenter-bar">
    <span class="presenter">pale harbor entertainment</span>
    <span class="presents">presents</span>
  </header>

  <div class="title title-top">Harbor Laughs Live</div>
  <h1 class="title title-main">Gets Real Honest</h1>
  <p class="hosted-by">a comedy show hosted by</p>

  <figure class="host-card left">
    <span class="clip"></span>
    <div class="host-photo" role="img" aria-label="Black and white portrait photo of host Zolo Brightwave">
      <span class="host-name">Zolo Brightwave</span>
    </div>
  </figure>
  <figure class="host-card right">
    <span class="clip"></span>
    <div class="host-photo" role="img" aria-label="Black and white portrait photo of host Marla Vintrow">
      <span class="host-name">Marla Vintrow</span>
    </div>
  </figure>

  <div class="rule rule-upper"></div>
  <p class="date-line">one night only! August 22, 2015 featuring</p>
  <p class="lineup lineup-1">Dov Pelletier • Rufus Kanderley • Otis Brambleworth</p>
  <p class="lineup lineup-2">Nina Velasko • Quillan • Jory Tamsett</p>
  <div class="rule rule-lower"></div>

  <p class="venue">@ Lantern Hall Theatre 48 Marlow St - Harborview, NY 10990</p>
  <p class="site">www.plgrvn.com</p>

  <div class="rule rule-bottom"></div>
</main>
</body>
</html>
```